Logo Tweak & Full Set of Stationery

We need a redesign / tweaking of Logo for rebranding of our company. We are Australia's largest installer of commercial fencing and high security infrastructure. We also have divisions in security and civil works (infrastrucuture).

We would like to see designs that incorporate black, white & blue. Revamp of current Diamond Logo (including HC) would be ideal but open to all ideas.

Design needs to portray a highly professional & corporate image.

Required:
- Tweak / Redesign of Logo
- Letterhead
- email Signature
- Business Cards
- Presentation Folder

Address fields should be interchangeable to accomodate multiple locations.

Website: www.harvillecorp.com.au
Updates

Due to short turn around time for project - Fee increased to $500 AUD Guaranteed

Thanks

Designs are looking good
I have emailed those submitted thus far to the board to start short listing.

Please do not take offence if your design is eliminated as part of this process  - there are so many great concepts and if is difficult to pick between them.

Thanks
Dustin

Target Market(s)

Tier 1 / 2 Builders (ie.. Brick Arch Peter Farley) and Government related bodies

Industry/Entity Type

Security

Requirements
Must have
• Company Name: Harville Corp

Tag Line: Fencing * Security * Civil

Logo

```html
<!DOCTYPE html>
<html lang="en">
<head>
<meta charset="utf-8">
<title>Harville Corp Stationery</title>
<link href="https://fonts.googleapis.com/css2?family=Tinos:wght@400;700&display=swap" rel="stylesheet">
<style>
  :root {
    --board-blue: #4268b9;
    --brand-blue: #4a72c4;
    --ink: #1d1d1f;
    --card-black: #19191b;
    --folder-black: #171719;
    --paper: #ffffff;
    --tint-blue: rgba(74, 114, 196, 0.28);
    --tint-grey: rgba(120, 120, 130, 0.18);
    --shade-navy: rgba(22, 30, 70, 0.9);
    --shade-grey: rgba(60, 60, 64, 0.55);
  }
  * { margin: 0; padding: 0; box-sizing: border-box; }
  html, body { width: 1200px; height: 900px; overflow: hidden; }
  body {
    position: relative;
    background: var(--board-blue);
    font-family: "Tinos", "Times New Roman", serif;
    color: var(--ink);
  }
  .header-band {
    position: absolute; left: 0; top: 0; width: 1200px; height: 188px;
    background: var(--paper);
    box-shadow: 0 4px 6px rgba(0,0,0,0.45);
  }
  .brand { position: absolute; display: flex; align-items: center; white-space: nowrap; font-weight: 700; z-index: 2; }
  .brand-square { display: inline-block; background: var(--brand-blue); flex: none; }
  .brand-main { left: 70px; top: 62px; font-size: 45px; gap: 45px; }
  .brand-main .brand-square { width: 42px; height: 42px; }

  .signature { position: absolute; left: 556px; top: 70px; width: 600px; height: 110px; }
  .signature .brand { left: 16px; top: 2px; font-size: 26px; gap: 24px; }
  .signature .brand-square { width: 26px; height: 26px; }
  .signature-rule { position: absolute; left: 156px; top: 38px; width: 436px; height: 1px; background: var(--brand-blue); }
  .signature-name { position: absolute; left: 329px; top: 12px; font-size: 14px; white-space: nowrap; }
  .signature-name strong { color: var(--brand-blue); font-size: 19px; margin-right: 6px; }
  .signature-contact { position: absolute; left: 331px; top: 48px; font-size: 13px; line-height: 17.5px; white-space: nowrap; }
  .signature-contact .bold { font-weight: 700; }
  .signature-contact .web { color: var(--brand-blue); font-size: 14px; }

  .watermark-area { position: absolute; z-index: 1; pointer-events: none; }

  .letterhead {
    position: absolute; left: 180px; top: 238px; width: 420px; height: 600px;
    background: var(--paper); box-shadow: 3px 4px 6px rgba(0,0,0,0.4);
    overflow: hidden;
  }
  .letterhead .brand { left: 36px; top: 46px; font-size: 13px; gap: 12px; }
  .letterhead .brand-square { width: 16px; height: 16px; }
  .letterhead .watermark-area {
    left: 180px; top: 330px; width: 280px; height: 290px;
    background:
      radial-gradient(ellipse at 65% 30%, var(--tint-blue), rgba(74,114,196,0) 65%),
      radial-gradient(ellipse at 45% 80%, var(--tint-grey), rgba(120,120,130,0) 65%);
  }

  .business-card {
    position: absolute; left: 67px; width: 256px; height: 142px;
    background: var(--card-black); color: #fff;
    box-shadow: 3px 4px 6px rgba(0,0,0,0.45);
    overflow: hidden;
  }
  .card-front { top: 423px; }
  .card-back { top: 585px; }
  .business-card .brand { font-size: 13px; gap: 14px; }
  .business-card .brand-square { width: 18px; height: 18px; }
  .card-front .brand { left: 22px; top: 23px; }
  .card-back .brand { left: 22px; top: 42px; font-size: 15px; gap: 16px; }
  .business-card .watermark-area {
    left: 150px; top: 20px; width: 140px; height: 130px;
    background:
      radial-gradient(ellipse at 70% 30%, var(--shade-navy), rgba(22,30,70,0) 60%),
      radial-gradient(ellipse at 55% 75%, var(--shade-grey), rgba(60,60,64,0) 60%);
  }
  .card-person { position: absolute; left: 53px; top: 57px; font-size: 7px; white-space: nowrap; color: #ddd; z-index: 2; }
  .card-person strong { color: var(--brand-blue); font-size: 10px; margin-right: 4px; }
  .card-details { position: absolute; left: 53px; top: 72px; font-size: 6.5px; line-height: 8.5px; color: #ddd; white-space: nowrap; z-index: 2; }
  .card-details .bold { font-weight: 700; color: #fff; }
  .card-details .web { color: var(--brand-blue); margin-top: 5px; }
  .card-tagline { position: absolute; left: 60px; top: 87px; font-size: 11px; color: #eee; white-space: nowrap; z-index: 2; }

  .folder {
    position: absolute; left: 678px; top: 237px; width: 426px; height: 603px;
    background: var(--folder-black); box-shadow: 3px 4px 6px rgba(0,0,0,0.45);
    overflow: hidden;
  }
  .folder .brand { left: 64px; top: 232px; font-size: 17px; color: #fff; gap: 22px; }
  .folder .brand-square { width: 22px; height: 22px; }
  .folder .watermark-area {
    left: 90px; top: 200px; width: 380px; height: 420px;
    background:
      radial-gradient(ellipse at 65% 30%, var(--shade-navy), rgba(22,30,70,0) 62%),
      radial-gradient(ellipse at 50% 78%, var(--shade-grey), rgba(60,60,64,0) 62%);
  }
</style>
</head>
<body>
  <header class="header-band">
    <div class="brand brand-main"><span class="brand-square"></span>Harville Corp</div>

    <div class="signature">
      <div class="brand"><span class="brand-square"></span>Harville Corp</div>
      <div class="signature-rule"></div>
      <div class="signature-name"><strong>Dustin Marsh</strong> Chief Financial Officer</div>
      <div class="signature-contact">
        <div class="bold">Mobile. 0413 552 817 | Phone. +61 2 9555 0143</div>
        <div>Free Call. 1800 555 219 | Fax. +61 2 9555 0178</div>
        <div class="web">www.harvillecorp.com.au</div>
      </div>
    </div>
  </header>

  <section class="letterhead">
    <div class="brand"><span class="brand-square"></span>Harville Corp</div>
    <div class="watermark-area" role="img" aria-label="Faint brand watermark area"></div>
  </section>

  <section class="business-card card-front">
    <div class="watermark-area" role="img" aria-label="Faint brand watermark area"></div>
    <div class="brand"><span class="brand-square"></span>Harville Corp</div>
    <div class="card-person"><strong>Dustin Marsh</strong> Chief Financial Officer</div>
    <div class="card-details">
      <div class="bold">Mobile. 0413 552 817</div>
      <div class="bold">Phone. +61 2 9555 0143</div>
      <div>Free Call. 1800 555 219</div>
      <div>Fax. +61 2 9555 0178</div>
      <div>Email. dmarsh@harvillecorp.com.au</div>
      <div class="web">www.harvillecorp.com.au</div>
    </div>
  </section>

  <section class="business-card card-back">
    <div class="watermark-area" role="img" aria-label="Faint brand watermark area"></div>
    <div class="brand"><span class="brand-square"></span>Harville Corp</div>
    <div class="card-tagline">Fencing ▪ Security ▪ Civil</div>
  </section>

  <section class="folder">
    <div class="watermark-area" role="img" aria-label="Large faint brand watermark area"></div>
    <div class="brand"><span class="brand-square"></span>Harville Corp</div>
  </section>
</body>
</html>
```